Business Card Design

I need a business card design for my law office based in Pasadena, California. I am a sole practitioner and I specialize in business transaction and litigation, probate and estate planning, taxation law, corporate and business formation, immigration and real estate. I want something that is simple, yet stands out.

A friend helped to create a logo about 6 years ago. I am open to new ideas to changing the logo.

Industry/Entity Type

Business

Contact Information for Business Card

Law Offices of Dorvan L. Mabry
842 W. Larkspur Ave., Suite 319
Pasadena, CA 90287
Tel: 626-555-0174
Fax: 626-555-0139
Email: dmabry@dlmlegalgroup.example

Attorney: Dorvan L. Mabry

```html
<!DOCTYPE html>
<html lang="en">
<head>
<meta charset="utf-8">
<title>Law Offices of Dorvan L. Mabry — Business Cards</title>
<link rel="stylesheet" href="https://fonts.googleapis.com/css2?family=Marcellus+SC&family=Lora:wght@400&display=swap">
<style>
  :root {
    --backdrop: #3b322e;
    --card: #f7f7f5;
    --ink: #1a1a1a;
    --ink-soft: #3a3a3a;
    --rule: #6d6d6d;
  }
  * { margin: 0; padding: 0; box-sizing: border-box; }
  html, body {
    width: 1200px;
    height: 716px;
    overflow: hidden;
    background: var(--backdrop);
  }
  .canvas {
    position: relative;
    width: 1200px;
    height: 716px;
  }
  .card {
    position: absolute;
    background: var(--card);
    box-shadow: 0 10px 24px rgba(0, 0, 0, 0.35);
    color: var(--ink);
  }

  /* Front card */
  .card--front {
    left: 70px;
    top: 80px;
    width: 500px;
    height: 286px;
  }
  .front__mark {
    position: absolute;
    left: 0;
    right: 0;
    top: 62px;
    display: flex;
    align-items: center;
    justify-content: center;
    gap: 10px;
  }
  .mark__square {
    width: 14px;
    height: 14px;
    background: var(--ink);
  }
  .mark__name {
    font-family: "Lora", serif;
    font-size: 15px;
    color: var(--ink);
  }
  .front__rule {
    position: absolute;
    left: 88px;
    width: 324px;
    height: 1px;
    background: var(--rule);
  }
  .front__rule--top { top: 126px; }
  .front__rule--bottom { top: 190px; }
  .front__kicker {
    position: absolute;
    left: 0;
    right: 0;
    top: 134px;
    text-align: center;
    font-family: "Lora", serif;
    font-size: 10px;
    letter-spacing: 0.32em;
    text-transform: uppercase;
    color: var(--ink-soft);
  }
  .front__name {
    position: absolute;
    left: 0;
    right: 0;
    top: 148px;
    text-align: center;
    font-family: "Marcellus SC", serif;
    font-size: 31px;
    letter-spacing: 0.02em;
    color: var(--ink);
  }

  /* Back card */
  .card--back {
    left: 620px;
    top: 300px;
    width: 520px;
    height: 297px;
  }
  .back__name {
    position: absolute;
    left: 36px;
    top: 30px;
    font-family: "Marcellus SC", serif;
    font-size: 21px;
    color: var(--ink);
  }
  .back__title {
    position: absolute;
    left: 36px;
    top: 58px;
    font-family: "Lora", serif;
    font-size: 10px;
    color: var(--ink-soft);
  }
  .back__contact {
    position: absolute;
    left: 36px;
    top: 128px;
    font-family: "Lora", serif;
    font-size: 11px;
    line-height: 15px;
    color: var(--ink);
    list-style: none;
  }
  .back__rule {
    position: absolute;
    left: 36px;
    top: 182px;
    width: 160px;
    height: 1px;
    background: var(--rule);
  }
  .back__address {
    position: absolute;
    left: 36px;
    top: 190px;
    font-family: "Lora", serif;
    font-size: 11px;
    line-height: 15px;
    font-style: normal;
    color: var(--ink);
  }
  .back__mark {
    position: absolute;
    right: 40px;
    bottom: 40px;
    display: flex;
    align-items: center;
    gap: 10px;
  }
  .back__mark .mark__square {
    width: 40px;
    height: 40px;
  }
</style>
</head>
<body>
<main class="canvas">

  <section class="card card--front" aria-label="Business card front">
    <div class="front__mark">
      <span class="mark__square" aria-hidden="true"></span>
      <span class="mark__name">Dorvan L. Mabry</span>
    </div>
    <div class="front__rule front__rule--top"></div>
    <p class="front__kicker">Law Offices of</p>
    <h1 class="front__name">Dorvan L. Mabry</h1>
    <div class="front__rule front__rule--bottom"></div>
  </section>

  <section class="card card--back" aria-label="Business card back">
    <h2 class="back__name">Dorvan L. Mabry</h2>
    <p class="back__title">Attorney / Lawyer</p>
    <ul class="back__contact">
      <li>626-555-0174</li>
      <li>626-555-0139</li>
      <li>dmabry@dlmlegalgroup.example</li>
    </ul>
    <div class="back__rule"></div>
    <address class="back__address">
      842 W. Larkspur Ave., Suite 319<br>
      Pasadena, CA 90287
    </address>
    <div class="back__mark">
      <span class="mark__square" aria-hidden="true"></span>
      <span class="mark__name">Dorvan L. Mabry</span>
    </div>
  </section>

</main>
</body>
</html>
```